New modern website for Kerbline Groundworks

Hi we are an existing company that has a current website http://www.kerblinegroundworks.co.nz/ we are looking to get a new vibrant looking website designed to take us further and gain more customers. We are after a simple easy to use website that does not confuse but we want to make an impact and stand out from the rest

Target Market(s)

Homeowners And Commercial Businesses

Industry/Entity Type

It Company

Coding

Coded - Design and coding required

Number of Pages Required

2 page

```html
<!DOCTYPE html>
<html lang="en">
<head>
<meta charset="utf-8">
<title>Kerbline Groundworks</title>
<link href="https://fonts.googleapis.com/css2?family=Raleway:wght@300;400;600;700;800&family=Open+Sans:wght@400;600;700&display=swap" rel="stylesheet">
<style>
:root{
  --yellow:#f9b233;
  --yellow-deep:#f39c12;
  --ink:#222222;
  --text:#444444;
  --muted:#777777;
  --white:#ffffff;
  --line:#d9d9d9;
}
*{box-sizing:border-box;margin:0;padding:0}
html,body{width:1200px;height:2946px;overflow:hidden}
body{position:relative;background:var(--white);font-family:"Open Sans",Arial,sans-serif;color:var(--text)}
.band{position:absolute;left:0;width:1200px}

/* header */
.site-header{top:0;height:63px;background:var(--white)}
.brand{position:absolute;left:251px;top:20px;display:flex;align-items:center;gap:8px}
.brand-mark{width:12px;height:12px;background:var(--ink)}
.brand-name{font-family:"Raleway",sans-serif;font-weight:800;font-size:17px;color:var(--ink);letter-spacing:.5px;text-transform:uppercase}
.header-contact{position:absolute;top:18px;display:flex;gap:10px;align-items:flex-start;font-size:10px;line-height:13px;color:var(--ink)}
.header-contact b{font-size:11px;display:block}
.contact-phone{left:700px}
.contact-post{left:862px}

/* nav */
.main-nav{top:63px;height:39px;background:var(--yellow)}
.nav-links{position:absolute;left:249px;top:0;display:flex;gap:30px;height:39px;align-items:center}
.nav-links span{font-weight:700;font-size:11.5px;color:var(--ink)}
.social{position:absolute;left:738px;top:0;height:39px;display:flex;align-items:center;gap:6px}
.social-label{font-weight:700;font-size:11.5px;color:var(--ink);margin-right:8px}
.social i{display:block;width:25px;height:25px;border-radius:50%;background:var(--white)}

/* hero */
.hero{top:102px;height:436px;background:linear-gradient(180deg,#9fb4c6 0%,#b7a77a 45%,#7d6c4e 100%)}
.hero-rule{top:538px;height:5px;background:var(--yellow)}
.hero-copy{position:absolute;left:560px;top:352px;width:391px;text-align:right;color:var(--white)}
.hero-title{font-family:"Raleway",sans-serif;font-weight:800;font-size:26px;line-height:28px}
.hero-sub{font-family:"Raleway",sans-serif;font-weight:800;font-size:16px;color:var(--yellow)}
.hero-text{font-size:12px;line-height:18px;margin-top:10px}
.btn-outline{display:inline-block;margin-top:12px;border:1px solid var(--yellow);color:var(--yellow);font-size:11px;padding:0 16px;height:30px;line-height:28px;text-transform:uppercase}
.hero-dots{position:absolute;left:908px;top:517px;display:flex;gap:3px}
.hero-dots i{width:5px;height:5px;border-radius:50%;background:var(--white)}

/* headings */
.section-title{font-family:"Raleway",sans-serif;font-weight:300;font-size:24px;line-height:27px;color:var(--ink);text-transform:uppercase;text-align:center}
.section-title b{font-weight:800}
.section-title.accent,.section-title.accent b{color:var(--yellow)}
.title-rule{width:180px;height:1px;background:rgba(255,255,255,.6)}
.title-rule.dark{background:var(--line)}
.btn-solid{display:inline-block;background:var(--yellow);color:var(--white);font-size:9.5px;font-weight:700;padding:0 14px;height:26px;line-height:26px;text-transform:uppercase}
.btn-ghost{display:inline-block;border:1px solid rgba(255,255,255,.8);color:var(--white);font-size:11px;padding:0 20px;height:30px;line-height:28px;text-transform:uppercase}
.btn-ghost b{color:var(--yellow)}

/* features */
.features{top:543px;height:395px}
.features .section-title{position:absolute;top:42px;left:0;width:1200px}
.feature{position:absolute;top:130px;width:220px;text-align:center}
.feature-icon{width:70px;height:70px;margin:0 auto;border-radius:50%;background:var(--yellow-deep);border:3px solid var(--white);box-shadow:0 0 0 3px var(--yellow-deep);display:flex;align-items:center;justify-content:center}
.feature h3{font-weight:700;font-size:12.5px;color:var(--ink);margin-top:30px;text-transform:uppercase;white-space:nowrap}
.feature p{font-size:9.5px;line-height:12px;color:var(--text);margin:10px auto 0;width:200px;height:50px}
.feature .btn-solid{margin-top:15px}

/* services */
.services{top:938px;height:299px;background:linear-gradient(90deg,#3a3630,#24211e 45%,#3b3732)}
.services .section-title{position:absolute;top:42px;left:0;width:1200px}
.services .title-rule{position:absolute;top:80px;left:510px}
.services-text{position:absolute;left:250px;top:106px;width:700px;text-align:center;color:#e8e8e8;font-family:"Raleway",sans-serif;font-weight:400;font-size:15.5px;line-height:20px}
.services .btn-ghost{position:absolute;left:541px;top:230px}

/* specialist */
.specialist{top:1237px;height:403px}
.specialist .section-title{position:absolute;top:47px;left:0;width:1200px}
.body-copy{position:absolute;left:249px;width:702px;text-align:center;font-size:10.5px;line-height:16px;color:var(--text)}
.sub-heading{position:absolute;left:0;width:1200px;top:214px;text-align:center;font-family:"Raleway",sans-serif;font-weight:400;font-size:25px;color:var(--ink)}
.specialist .btn-solid{position:absolute;left:541px;top:340px;width:118px;text-align:center;height:28px;line-height:28px}

/* projects */
.projects{top:1640px;height:501px;background:linear-gradient(135deg,#2f2c28,#1f1d1b 50%,#34302a)}
.projects .section-title.accent{position:absolute;top:42px;left:0;width:1200px;font-size:23px}
.projects .title-rule{position:absolute;top:77px;left:510px}
.projects .tagline{position:absolute;top:110px;left:0;width:1200px;color:var(--white);font-size:22px}
.thumb{position:absolute;width:121px;height:90px;border:2px solid #8a7a55}
.thumb.active{border-color:var(--white)}
.projects .btn-ghost{position:absolute;left:524px;top:426px;width:152px;text-align:center}

/* testimonials */
.testimonials{top:2141px;height:310px}
.testimonials .section-title{position:absolute;top:40px;left:0;width:1200px}
.testimonials .title-rule{position:absolute;top:76px;left:540px;width:120px}
.quote{position:absolute;left:270px;top:94px;width:660px;text-align:center;font-size:10px;line-height:16px;color:var(--text)}
.quote-sign{position:absolute;left:0;width:1200px;top:195px;text-align:center;font-size:10px;color:var(--text)}
.quote-name{position:absolute;left:0;width:1200px;top:225px;text-align:center;font-family:"Raleway",sans-serif;font-weight:800;font-size:16px;color:var(--ink)}
.quote-meta{position:absolute;left:0;width:1200px;top:258px;text-align:center;font-size:10px;color:var(--muted)}

/* contact */
.contact{top:2451px;height:452px;background:linear-gradient(180deg,#2c2925,#201e1b)}
.contact-line{position:absolute;top:50px;font-size:14px;color:var(--white);width:300px}
.contact-line b{font-weight:700}
.contact-line.phone{left:249px}
.contact-line.email{left:651px;text-align:right}
.contact-title{position:absolute;top:34px;left:0;width:1200px;text-align:center;font-family:"Raleway",sans-serif;font-weight:400;font-size:30px;color:var(--yellow)}
.contact-title b{font-weight:700}
.contact-sub{position:absolute;top:106px;left:0;width:1200px;text-align:center;font-family:"Raleway",sans-serif;font-weight:300;font-size:21px;color:var(--white)}
.field{position:absolute;border:1px solid var(--yellow);color:#8d8a86;font-size:7.5px;text-transform:uppercase;padding:9px 10px}
.btn-send{position:absolute;left:534px;top:391px;width:132px;height:30px;line-height:28px;border:1px solid var(--yellow);color:var(--white);font-size:9px;text-align:center;text-transform:uppercase}

/* footer */
.site-footer{top:2903px;height:43px;background:var(--yellow);font-size:9.5px;color:var(--ink)}
.site-footer span{position:absolute;top:15px}
</style>
</head>
<body>

<header class="band site-header">
  <div class="brand"><span class="brand-mark"></span><span class="brand-name">Kerbline Groundworks</span></div>
  <div class="header-contact contact-phone">
    <svg width="18" height="18" viewBox="0 0 24 24"><path d="M6.6 10.8c1.4 2.8 3.8 5.1 6.6 6.6l2.2-2.2c.3-.3.7-.4 1-.2 1.1.4 2.3.6 3.6.6.6 0 1 .4 1 1V20c0 .6-.4 1-1 1C10.6 21 3 13.4 3 4c0-.6.4-1 1-1h3.5c.6 0 1 .4 1 1 0 1.3.2 2.5.6 3.6.1.3 0 .7-.2 1l-2.3 2.2z" fill="#222"/></svg>
    <div><b>09 555 0142</b>info@kerblinegroundworks.co.nz</div>
  </div>
  <div class="header-contact contact-post">
    <svg width="20" height="18" viewBox="0 0 24 22"><path d="M12 2 1 12h3v9h6v-6h4v6h6v-9h3z" fill="#222"/></svg>
    <div>PO Box 40217<b>Auckland NZ</b></div>
  </div>
</header>

<nav class="band main-nav">
  <div class="nav-links"><span>HOME</span><span>ABOUT US</span><span>OUR SERVICES</span><span>PROJECTS</span><span>CONTACT US</span></div>
  <div class="social"><span class="social-label">FOLLOW US ON:</span><i></i><i></i><i></i><i></i></div>
</nav>

<section class="band hero" role="img" aria-label="Photo of a winding asphalt road through golden grassland below blue hills"></section>
<div class="hero-copy">
  <div class="hero-title">KERBLINE GROUNDWORKS</div>
  <div class="hero-sub">PROJECT LTD</div>
  <p class="hero-text">Leading the way for asphalt &amp; concrete works throughout the Auckland region, Warren and the local team from Kerbline Groundworks will go the extra mile for your project.</p>
  <span class="btn-outline">Learn More</span>
</div>
<div class="hero-dots"><i></i><i></i><i></i><i></i><i></i></div>
<div class="band hero-rule"></div>

<section class="band features">
  <h2 class="section-title">The trusted <b>name for</b> all <b>concrete</b> &amp;<br><b>asphalt</b> paving in <b>Auckland</b></h2>
  <div class="feature" style="left:234px">
    <div class="feature-icon"><svg width="38" height="34" viewBox="0 0 24 22"><path d="M12 2 1 12h3v9h6v-6h4v6h6v-9h3z" fill="none" stroke="#fff" stroke-width="1.6"/></svg></div>
    <h3>Concreting &amp; Asphalt</h3>
    <p>When it comes to all asphalt services, you can rest assured we will work around your schedule, requirements and budget. Servicing throughout Auckland.</p>
    <span class="btn-solid">Learn More</span>
  </div>
  <div class="feature" style="left:495px">
    <div class="feature-icon"></div>
    <h3>Additional Services</h3>
    <p>As part of our asphalt services, we are proud to offer a range of related services to our clients in the eastern suburbs and greater Auckland.</p>
    <span class="btn-solid">Learn More</span>
  </div>
  <div class="feature" style="left:752px">
    <div class="feature-icon"><svg width="50" height="50" viewBox="0 0 56 56"><circle cx="28" cy="28" r="25" fill="#fff"/><circle cx="28" cy="28" r="18" fill="none" stroke="#f39c12" stroke-width="2"/></svg></div>
    <h3>Our Expertise</h3>
    <p>We have a reputation with clients in and around Auckland for achieving great results on time and within budget every time. We are proud to share our years...</p>
    <span class="btn-solid">Learn More</span>
  </div>
</section>

<section class="band services" role="img" aria-label="Darkened photo of a truck on a paving site">
  <h2 class="section-title accent">View our <b>Services</b></h2>
  <div class="title-rule"></div>
  <p class="services-text">Complete asphalt services for your next project in Auckland. As your local one-stop shop you will receive durable solutions by calling on Kerbline Groundworks for all asphalt services. Arriving at your property in Auckland at an agreed upon time, we promise to leave no mess behind, only quality results. So please feel free to call us today<br>to discuss what we can do for your project.</p>
  <span class="btn-ghost">View <b>Details</b></span>
</section>

<section class="band specialist">
  <h2 class="section-title">Your one-stop <b>specialist</b> for <b>driveway<br>construction</b> in Auckland</h2>
  <p class="body-copy" style="top:128px">Leading the way for asphalt and concrete works throughout the Auckland region, Warren and the local team from Kerbline Groundworks will go the extra mile for your project. We can complete high quality asphalt paving, driveway construction and more for our clients. Ensuring the highest standards for safety and quality, we will work with you<br>directly throughout all aspects of the job.</p>
  <h3 class="sub-heading">Personalized service</h3>
  <p class="body-copy" style="top:247px">Dedicated to quality results for your asphalt paving or driveway construction project in Auckland, we take a personalized approach on every project. Ensuring a result that doesn't break the bank, we offer a range of terrific financing options, which we can discuss with you when you call. We are happy to provide more information and discuss all your requirements with you. Feel free to browse our gallery to view photos of our completed work.</p>
  <span class="btn-solid">Learn More</span>
</section>

<section class="band projects" role="img" aria-label="Darkened photo of paving machinery">
  <h2 class="section-title accent">View our <b>Projects</b></h2>
  <div class="title-rule"></div>
  <h3 class="section-title tagline">For <b>residential</b> driveways and <b>commercial</b><br>paving in <b>Auckland</b></h3>
  <div class="thumb" style="left:249px;top:192px;background:linear-gradient(#7d8b6a,#8a8a86)" role="img" aria-label="Finished concrete driveway"></div>
  <div class="thumb active" style="left:393px;top:192px;background:linear-gradient(#5d6a4e,#6c6c68)" role="img" aria-label="Driveway beside a house"></div>
  <div class="thumb" style="left:537px;top:192px;background:linear-gradient(#a09a90,#b4534a)" role="img" aria-label="Fresh asphalt car park"></div>
  <div class="thumb" style="left:681px;top:192px;background:linear-gradient(#8f8a83,#2f2f33)" role="img" aria-label="New black asphalt driveway"></div>
  <div class="thumb" style="left:825px;top:192px;background:linear-gradient(#657048,#3c3b38)" role="img" aria-label="Sealed driveway with hedge"></div>
  <div class="thumb" style="left:249px;top:306px;background:linear-gradient(#55504a,#c1502f)" role="img" aria-label="Site with traffic cones"></div>
  <div class="thumb" style="left:393px;top:306px;background:linear-gradient(#3a3631,#a88a4a)" role="img" aria-label="Commercial entrance paving"></div>
  <div class="thumb" style="left:537px;top:306px;background:linear-gradient(#9a9aa0,#a33b2f)" role="img" aria-label="Work truck on site"></div>
  <div class="thumb" style="left:681px;top:306px;background:linear-gradient(#aaa49b,#7a6e60)" role="img" aria-label="Crew laying concrete"></div>
  <div class="thumb" style="left:825px;top:306px;background:linear-gradient(#b8b0a2,#c7a14a)" role="img" aria-label="Roller on asphalt"></div>
  <span class="btn-ghost">View All <b>Projects</b></span>
</section>

<section class="band testimonials">
  <h2 class="section-title">What <b>clients</b> say...</h2>
  <div class="title-rule dark"></div>
  <p class="quote">Can you please pass on my thanks to Warren and Tomas for the outstanding service and work done at our property (it looks amazing). Although there were some issues (heavy rain) we have throughout this whole process been totally confident in their professional attitude and work ethic. Both Helena and I work in the service industry and I must say that the service and care we have received from all we have dealt with in your company is hard to find these days. We have recommended you to ALL of our friends and work colleagues. Please pass on my thanks to all concerned.</p>
  <p class="quote-sign">Many Thanks,</p>
  <p class="quote-name">MARION</p>
  <p class="quote-meta">Paula and Helena, Paula Brecken &nbsp;|&nbsp; Design Manager – Printhaus Studio</p>
</section>

<section class="band contact" role="img" aria-label="Dark photo of a road at dusk">
  <p class="contact-line phone">Phone: &nbsp;<b>09 555 0142</b></p>
  <h2 class="contact-title">Contact <b>US</b></h2>
  <p class="contact-line email">Email:kerblinegroundworks.co.nz</p>
  <h3 class="contact-sub">Call for Quality Paving Services in Auckland</h3>
  <div class="field" style="left:249px;top:153px;width:222px;height:28px">Your Name</div>
  <div class="field" style="left:489px;top:153px;width:222px;height:28px">Your Email</div>
  <div class="field" style="left:729px;top:153px;width:222px;height:28px">Phone</div>
  <div class="field" style="left:249px;top:201px;width:702px;height:170px">The Message</div>
  <div class="btn-send">Send Your Message</div>
</section>

<footer class="band site-footer">
  <span style="left:251px">Copyright © kerblinegroundworks. All right Reserved</span>
  <span style="left:746px">Design &amp; developed by Brightfold Digital</span>
</footer>

</body>
</html>
```